Thrifty Haul: Junk Removal - Website Design

We need a design and uploaded to Webnestor.com. I enclosed our postcard for reference too. I need a contact from at the top right so I can get leads.

Here are the sites I like:

https://haulvantix.com/
https://www.1800trashpro.com
https://www.campusmoversclearout.com/junk-removal/
http://ahavenforkin.com/
http://www.drivelark.com/alternate/
https://www.servicemenautogifts.org/
http://www.vehiclesforheroes.org/indexj/

Coding

Coded - Design and coding required

Number of Pages Required

1 page

```html
<!DOCTYPE html>
<html lang="en">
<head>
<meta charset="utf-8">
<title>Thrifty Haul – Junk Removal</title>
<link rel="stylesheet" href="https://fonts.googleapis.com/css2?family=Montserrat:wght@300;400;500;600;700;800&family=Oswald:wght@400;500;600&display=swap">
<style>
:root{
  --green:#7cc22a;
  --blue:#0d4a97;
  --ink:#222;
  --muted:#555;
  --mint:#e3f4f3;
  --white:#fff;
}
*{box-sizing:border-box;margin:0;padding:0}
html,body{width:1200px;height:3287px;overflow:hidden}
body{font-family:"Montserrat",sans-serif;color:var(--ink);background:var(--white);position:relative}
.wrap{position:absolute;left:132px;right:132px}
.btn{display:inline-block;background:var(--green);color:var(--white);font-family:"Oswald",sans-serif;font-size:14px;letter-spacing:.3px;text-transform:uppercase;border-radius:22px;padding:0 26px;line-height:38px;text-decoration:none}
.g{color:var(--green)}

/* header */
.header{position:absolute;top:0;left:0;width:1200px;height:80px}
.brand{position:absolute;left:132px;top:16px;font-family:"Oswald",sans-serif;font-weight:600;font-size:38px;color:var(--green);letter-spacing:.5px}
.tagline{position:absolute;right:300px;top:22px;text-align:right;font-size:15px}
.tagline small{display:block;font-size:12px;color:var(--muted);margin-top:2px}
.header .btn{position:absolute;right:132px;top:22px;line-height:36px}
.helpbar{position:absolute;top:80px;left:0;width:500px;height:40px;background:var(--blue);clip-path:polygon(0 0,465px 0,500px 40px,0 40px);color:#fff;font-size:15px;padding-left:132px;line-height:40px}
.helpbar b{color:var(--green);font-weight:600}
.helpbar svg{vertical-align:-5px;margin:0 3px}
.nav{position:absolute;top:80px;right:132px;height:40px;display:flex;gap:36px;font-family:"Oswald",sans-serif;font-size:14px;text-transform:uppercase;line-height:40px}
.nav a{color:var(--ink);text-decoration:none;position:relative}
.nav a.active::before{content:"";position:absolute;left:-8px;right:-8px;top:0;height:2px;background:var(--green)}
.rule{position:absolute;top:119px;left:500px;right:0;height:1px;background:#e2e2e2}

/* hero */
.hero{position:absolute;top:120px;left:0;width:1200px;height:480px;background:linear-gradient(100deg,#3b4a5a 0%,#6a6258 35%,#c8702a 60%,#8b5636 80%,#6c7784 100%)}
.hero h1{position:absolute;left:132px;top:128px;font-weight:800;font-size:50px;line-height:54px;color:#fff}
.hero h1 span{display:block;color:var(--green);font-size:58px}
.hero p{position:absolute;left:130px;top:260px;color:#fff;font-size:15px}
.hero .btn{position:absolute;left:132px;top:303px}
.arrow{position:absolute;width:26px;height:26px}

/* intro */
.intro{top:676px;text-align:center;font-size:15px;line-height:23px;color:#333}
.intro b{font-weight:700}
.intro h2{font-family:"Oswald",sans-serif;font-weight:500;font-size:40px;color:var(--green);margin-top:24px;letter-spacing:.3px}
.about-photo{position:absolute;left:132px;top:822px;width:468px;height:332px;background:linear-gradient(135deg,#c9cdd2,#e8722a 55%,#5c5f66)}
.about-text{position:absolute;left:647px;top:838px;width:421px;color:var(--muted)}
.about-text .lead{font-size:15.5px;line-height:22px;margin-bottom:20px;padding-right:10px}
.about-text p{font-size:11px;line-height:19px;margin-bottom:18px}
.about-text .btn{margin-top:8px}

/* why */
.why{position:absolute;top:1223px;left:0;width:1200px;height:414px;background:var(--blue);color:#fff;text-align:center}
.why h2{font-size:30px;font-weight:700;margin-top:70px}
.features{position:absolute;left:120px;top:156px;display:grid;grid-template-columns:repeat(4,240px)}
.feature{font-size:15px;line-height:23px}
.feature span{display:block;width:180px;margin:0 auto}
.feature svg{display:block;margin:0 auto 12px}
.why .btn{position:absolute;left:520px;top:294px}

/* services */
.services{top:1710px;text-align:center}
.services h2{font-size:31px;font-weight:700}
.services p.sub{font-size:15px;margin-top:2px}
.grid{position:absolute;left:132px;top:1803px;width:936px;height:439px;display:grid;grid-template-columns:repeat(3,1fr);grid-template-rows:220px 219px}
.cell{position:relative;background:var(--mint);text-align:center;padding-top:34px}
.cell h3{font-size:20px;font-weight:700;margin-bottom:14px}
.cell p{font-size:11.5px;line-height:19px;color:var(--muted);padding:0 28px;margin-bottom:18px}
.photo-a{background:linear-gradient(135deg,#8a6a4f,#c7b9a0 50%,#5e4736)}
.photo-b{background:linear-gradient(135deg,#6f6a66,#9b4a2c 50%,#3f3a38)}
.photo-c{background:linear-gradient(135deg,#c9b18f,#8e7358 50%,#4b5a6b)}
.notch{position:absolute;left:50%;bottom:0;margin-left:-10px;border:10px solid transparent;border-bottom-color:var(--mint)}

/* booking */
.booking{position:absolute;top:2322px;left:0;width:1200px;height:487px;background:linear-gradient(120deg,#1a55a3,#0d4a97 60%,#0b3f86);color:#fff;text-align:center}
.booking h2{font-size:31px;font-weight:700;margin-top:66px}
.booking h2 .save{font-weight:300;color:var(--green);font-size:42px;vertical-align:-2px}
.booking h2 sup{font-size:16px;color:var(--green)}
.booking .note{font-size:12px;margin-top:4px}
.form{position:absolute;left:252px;top:166px;width:696px}
.row{display:flex;gap:24px}
.field{flex:1;height:40px;border:1px solid rgba(255,255,255,.6);font-size:12px;text-align:left;padding:12px 18px}
.field.msg{height:96px;margin-top:24px}
.booking .btn{position:absolute;left:536px;top:366px;padding:0 32px}

/* map */
.map{position:absolute;top:2809px;left:0;width:1200px;height:431px;background:linear-gradient(180deg,#ececef,#e2e4e8)}
.card{position:absolute;left:420px;top:141px;width:360px;height:159px;background:#fff;text-align:center;padding-top:30px;box-shadow:0 2px 10px rgba(0,0,0,.1)}
.card h4{color:var(--green);font-size:15px;font-weight:700}
.card .addr{font-size:12px;margin-top:4px}
.card .line{width:80px;height:1px;background:#ddd;margin:14px auto}
.card .call{color:var(--green);font-size:20px;font-weight:500}
.card .mail{font-size:12px;margin-top:4px}

/* footer */
.footer{position:absolute;top:3240px;left:0;width:1200px;height:47px;background:var(--blue);color:#fff;font-family:"Oswald",sans-serif;font-size:12px;line-height:47px;padding-left:132px}
.social{position:absolute;right:132px;top:11px;display:flex;gap:12px}
.social span{width:26px;height:26px;border:1px solid #fff;border-radius:50%}
</style>
</head>
<body>

<header class="header">
  <div class="brand">THRIFTY HAUL</div>
  <div class="tagline">Full Service <span class="g">Junk Removal</span><small>America's most trusted name</small></div>
  <a class="btn" href="#book">Get an estimate</a>
</header>
<div class="helpbar">Need Help? Call Us:
  <svg width="22" height="22" viewBox="0 0 24 24" fill="none" stroke="#7cc22a" stroke-width="2"><circle cx="12" cy="12" r="10"/><path d="M8 7c0 5 4 9 9 9l1-2-3-2-1 1c-2-1-3-2-4-4l1-1-2-3z" fill="#7cc22a" stroke="none"/></svg><b>1.800.555.0142</b>
</div>
<nav class="nav">
  <a class="active" href="#">Home</a><a href="#">About</a><a href="#">Services</a><a href="#">Why Us?</a><a href="#">Careers</a><a href="#">Contact</a>
</nav>
<div class="rule"></div>

<section class="hero" role="img" aria-label="Photo of junk removal crew in orange safety uniforms beside a truck">
  <h1>No Contact<span>Junk Removal</span></h1>
  <p>Same Day Service + Best Price Guarantee</p>
  <a class="btn" href="#book">Schedule a pickup</a>
  <svg class="arrow" style="left:53px;top:207px" viewBox="0 0 26 26" fill="none" stroke="#fff" stroke-width="2"><circle cx="13" cy="13" r="11"/><path d="M18 13H8M12 9l-4 4 4 4"/></svg>
  <svg class="arrow" style="right:53px;top:207px" viewBox="0 0 26 26" fill="none" stroke="#fff" stroke-width="2"><circle cx="13" cy="13" r="11"/><path d="M8 13h10M14 9l4 4-4 4"/></svg>
</section>

<section class="wrap intro">
  <p><b class="g">Thrifty Haul</b> is a full-service junk removal company serving areas<br>across the united states, We're in your neighborhood.</p>
  <h2>15+ YEARS OF EXPERIENCE IN JUNK REMOVAL</h2>
</section>
<div class="about-photo" role="img" aria-label="Photo of two smiling workers in orange uniforms in front of a truck"></div>
<div class="about-text">
  <p class="lead">Lorem ipsum dolor sit amet, consectetur adipiscing elit, sed do eiusmod tempor incididunt</p>
  <p>Sed ut perspiciatis unde omnis iste natus error sit voluptatem accusantium doloremque laudantium, totam rem aperiam, eaque ipsa quae ab illo inventore veritatis et quasi architecto beatae vitae dicta sunt explicabo. Nemo enim ipsam voluptatem quia voluptas.</p>
  <p>Neque porro quisquam est, qui dolorem ipsum quia dolor sit amet, consectetur, adipisci velit, sed quia non numquam eius modi tempora incidunt ut labore.</p>
  <a class="btn" href="#">About us</a>
</div>

<section class="why">
  <h2>Why choose <span class="g">Thrifty Haul</span>?</h2>
  <div class="features">
    <div class="feature"><svg width="48" height="50" viewBox="0 0 48 50" fill="none" stroke="#7cc22a" stroke-width="2.5"><circle cx="24" cy="28" r="19"/><circle cx="24" cy="28" r="13"/><path d="M20 4h8M24 4v5M24 21v8h6"/></svg><span>On-time Junk Removal Service</span></div>
    <div class="feature"><svg width="48" height="50" viewBox="0 0 48 50" fill="none" stroke="#7cc22a" stroke-width="2.5"><path d="M24 3l5 5 7-1 1 7 6 4-3 6 3 6-6 4-1 7-7-1-5 5-5-5-7 1-1-7-6-4 3-6-3-6 6-4 1-7 7 1z"/><path d="M29 19c-1-2-3-3-5-3-3 0-5 2-5 4 0 5 10 3 10 8 0 3-2 4-5 4-2 0-4-1-5-3M24 13v23"/></svg><span>Up Front pricing, No Hidden charges</span></div>
    <div class="feature"><svg width="48" height="50" viewBox="0 0 48 50" fill="none" stroke="#7cc22a" stroke-width="2.5"><path d="M18 4h10l-2 8c8 4 14 14 12 30H8C6 26 12 16 20 12z"/><path d="M6 44h38"/><circle cx="30" cy="34" r="4"/></svg><span>Full-service Junk Removal</span></div>
    <div class="feature"><svg width="50" height="50" viewBox="0 0 50 50" fill="none" stroke="#7cc22a" stroke-width="2.5"><circle cx="25" cy="25" r="14"/><path d="M25 3v8M25 39v8M3 25h8M39 25h8M9 9l6 6M35 35l6 6M41 9l-6 6M15 35l-6 6"/><circle cx="21" cy="21" r="2"/><circle cx="29" cy="27" r="2"/><circle cx="23" cy="30" r="1.5"/></svg><span>Covid-19 Health and Safety Complaint</span></div>
  </div>
  <a class="btn" href="#book">Contact us today!</a>
</section>

<section class="wrap services">
  <h2>Full Service <span class="g">Junk Removal</span></h2>
  <p class="sub">All you have to do is point.</p>
</section>
<div class="grid">
  <div class="cell photo-a" role="img" aria-label="Photo of household items and boxes piled for removal"><span class="notch"></span></div>
  <div class="cell"><h3>Moving</h3><p>Ut enim ad minima veniam, quis nostrum exercitationem ullam corporis suscipit laboriosam, nisi ut aliquid ex ea</p><a class="btn" href="#">More</a></div>
  <div class="cell photo-b" role="img" aria-label="Photo of scrap metal being lifted by a grabber"><span class="notch"></span></div>
  <div class="cell"><h3>Residential</h3><p>Ut enim ad minima veniam, quis nostrum exercitationem ullam corporis suscipit laboriosam, nisi ut aliquid ex ea</p><a class="btn" href="#">More</a></div>
  <div class="cell photo-c" role="img" aria-label="Photo of two movers carrying cardboard boxes"></div>
  <div class="cell"><h3>Commercial</h3><p>Ut enim ad minima veniam, quis nostrum exercitationem ullam corporis suscipit laboriosam, nisi ut aliquid ex ea</p><a class="btn" href="#">More</a></div>
</div>
<svg class="arrow" style="left:53px;top:2010px" viewBox="0 0 26 26" fill="none" stroke="#0d4a97" stroke-width="2"><circle cx="13" cy="13" r="11"/><path d="M18 13H8M12 9l-4 4 4 4"/></svg>
<svg class="arrow" style="right:53px;top:2010px" viewBox="0 0 26 26" fill="none" stroke="#0d4a97" stroke-width="2"><circle cx="13" cy="13" r="11"/><path d="M8 13h10M14 9l4 4-4 4"/></svg>

<section class="booking" id="book">
  <h2>Book Today &amp; Save <span class="save"><sup>$</sup>25</span></h2>
  <p class="note">*Not valid on single item or minimum charge pickups.</p>
  <div class="form">
    <div class="row"><div class="field">Enter your name</div><div class="field">Email</div><div class="field">Phone</div></div>
    <div class="field msg">Message ...</div>
  </div>
  <a class="btn" href="#">Book now!</a>
</section>

<section class="map" role="img" aria-label="Street map showing the office location">
  <div class="card">
    <h4>Thrifty Haul</h4>
    <p class="addr">412 Larkin Avenue, Houston, TX 77002</p>
    <div class="line"></div>
    <p class="call">Call. 1.800.555.0142</p>
    <p class="mail">e. hello@thriftyhaul.com</p>
  </div>
</section>

<footer class="footer">© 2020 <span class="g">THRIFTY</span> HAUL. ALL RIGHTS RESERVED
  <div class="social"><span></span><span></span><span></span><span></span><span></span></div>
</footer>

</body>
</html>
```